Billboard Design for Modern Dispensary

Hello!
We need a eye-catching 12' x 24' billboard designed for a very successful, modern cannabis dispensary on the Oregon coast, United States. Because of rules, we cannot have any marijuana leafs or other cannabis related images (flower, joints, smoke, etc). We can use the words "Shop" or "Dispensary" - we cannot use the words "cannabis", "marijuana".

Some ideas we had are 3 words stacked on left or center of billboard - maybe across bottom we have horizontal logo and the following words - “South of bridge in Marlow Cove”
Another idea is to have a small bubble in bottom/top corner with image of our dog (face only) - with some words around it - like "BONUS Shop Dog" or "Cute Shop Dog" or "Best Shop Dog" or "Friendly Staff"

here's some 3 word examples:
ENJOY
YOUR
TRIP

or

FEEL
GOOD
JUST
AHEAD

or

GOOD
VIBES
ONLY

or

GOOD
TIMES
CHILL
VIBES

I have attached our logo. I have also included a stacked logo version (vertical, not horizontal). the formats are .EPS and .PDF - the logos were created in Affinity Design 2.x.

Our website is lunarwharf.com if you want to see more images, etc about our dispensary.

Artwork Requirements:
The billboard is 12' tall x 25' wide
The artwork needs to be 1”=1’ @ 300dpi
Please add 6” of bleed all around so your total artwork is 13”x26”
Final deliverable should be .Ai file.

Font styles to use
Sans Serif

Colors
0054AA
0677BA
7BADD7
CADEEF
E8F1F8

Requirements
Nice to have
• See the project description - we included some ideas to consider.
Should not have
• No cannabis images, like flower, cannabis leaves, paraphenlia, cartridges, joints, etc.

```html
<!DOCTYPE html>
<html lang="en">
<head>
<meta charset="utf-8">
<title>Lunar Wharf Billboard</title>
<link rel="stylesheet" href="https://fonts.googleapis.com/css2?family=Anton&family=Montserrat:wght@400;700&display=swap">
<style>
  :root {
    --backdrop: #7a7a7a;
    --brand-blue: #4e9ed8;
    --sign-white: #ffffff;
  }
  html, body {
    margin: 0;
    padding: 0;
    width: 929px;
    height: 1200px;
    overflow: hidden;
    background: var(--backdrop);
  }
  .canvas {
    position: relative;
    width: 929px;
    height: 1200px;
    display: flex;
    align-items: center;
    justify-content: center;
  }
  .billboard {
    width: 869px;
    height: 416px;
    display: flex;
    flex-direction: column;
    box-shadow: 0 10px 24px rgba(0, 0, 0, 0.35);
  }
  .headline-band {
    height: 127px;
    background: var(--brand-blue);
    display: flex;
    align-items: center;
    justify-content: center;
  }
  .headline {
    margin: 0;
    font-family: "Anton", sans-serif;
    font-weight: 400;
    font-size: 98px;
    line-height: 1;
    letter-spacing: 2px;
    color: var(--sign-white);
  }
  .brand-panel {
    flex: 1;
    background: var(--sign-white);
    display: flex;
    align-items: center;
    justify-content: center;
    gap: 22px;
  }
  .brand-dot {
    width: 150px;
    height: 150px;
    flex: none;
  }
  .brand-name {
    font-family: "Montserrat", sans-serif;
    font-weight: 400;
    font-size: 58px;
    letter-spacing: 1px;
    color: var(--brand-blue);
    white-space: nowrap;
  }
  .location-band {
    height: 83px;
    background: var(--brand-blue);
    display: flex;
    align-items: center;
    justify-content: center;
  }
  .location {
    margin: 0;
    font-family: "Montserrat", sans-serif;
    font-weight: 700;
    font-size: 37px;
    color: var(--sign-white);
    white-space: nowrap;
  }
</style>
</head>
<body>
  <main class="canvas">
    <section class="billboard">
      <div class="headline-band">
        <h1 class="headline">BEST SHOP PERIOD</h1>
      </div>
      <div class="brand-panel">
        <svg class="brand-dot" viewBox="0 0 150 150" aria-hidden="true">
          <circle cx="75" cy="75" r="68" fill="none" stroke="var(--brand-blue)" stroke-width="10"/>
        </svg>
        <span class="brand-name">LUNAR WHARF</span>
      </div>
      <div class="location-band">
        <p class="location">SOUTH OF BRIDGE IN MARLOW COVE</p>
      </div>
    </section>
  </main>
</body>
</html>
```